"Trade with Tilda" needs a funky and stylish business card

Hi my name is Tilda, I am an experienced Bidnest Prime Vendor with a 100% satisfaction rating and over 400 items sold

My business name and bidnest username is "Trade with Tilda" I sell other peoples items on Bidnest for a commission. The main items I sell are furniture and renovation/building salvage items such as used kitchens, bathrooms , window doors etc.

I will be promoting my service in real estate agent offices, storage facilities, removalists, building and renovating companies.

i believe selling on bidnest is a great way for people to recycle their used goods and salvageable materials and reduce waste and landfill.

Target Market(s)

people selling their homes, renovators, builders, downsizers

Industry/Entity Type

Real Estate

Contact Information for Business Card

Tilda Marlowe
0492716045

Logo Text

Trade with Tilda

Logo styles of interest
Wordmark Logo
Requirements
Must have
• the business card must feature the bidnest logo mentioning primevendorr gold ranked vendor I have attached a copy
Nice to have
• i would like to have the trade with tilda logo written in royal blue

```html
<!DOCTYPE html>
<html lang="en">
<head>
<meta charset="utf-8">
<title>Trade with Tilda – Business Card</title>
<link rel="stylesheet" href="https://fonts.googleapis.com/css2?family=Satisfy&family=Dancing+Script:wght@500;700&display=swap">
<style>
  :root {
    --page: #ffffff;
    --card-dark: #161616;
    --card-mid: #272727;
    --band-blue: #1d2f5c;
    --ring-blue: #1f3160;
    --royal-blue: #1a5cb0;
    --mark-grey: #7d877f;
    --text-light: #d8d8d8;
    --text-soft: #c6c6c6;
    --seal-gold: #b48a2c;
  }
  html, body {
    margin: 0;
    padding: 0;
    width: 1200px;
    height: 1000px;
    overflow: hidden;
    background: var(--page);
  }
  .canvas {
    position: relative;
    width: 1200px;
    height: 1000px;
    font-family: "Satisfy", "Dancing Script", "Segoe Script", "Brush Script MT", cursive;
  }
  .card {
    position: absolute;
    overflow: hidden;
    background: radial-gradient(ellipse at 50% 40%, var(--card-mid) 0%, var(--card-dark) 90%);
  }
  .card--front {
    left: 165px;
    top: 14px;
    width: 823px;
    height: 474px;
  }
  .card--back {
    left: 167px;
    top: 508px;
    width: 828px;
    height: 477px;
  }
  .brand-ring {
    position: absolute;
    left: 222px;
    top: 168px;
    width: 78px;
    height: 78px;
    border-radius: 50%;
    border: 10px solid var(--mark-grey);
    box-sizing: border-box;
  }
  .wordmark {
    position: absolute;
    left: 326px;
    top: 272px;
    margin: 0;
    font-size: 44px;
    font-weight: 400;
    line-height: 1.2;
    color: var(--royal-blue);
    white-space: nowrap;
  }
  .band {
    position: absolute;
    left: 0;
    top: 32px;
    width: 100%;
    height: 78px;
    background: var(--band-blue);
  }
  .holder-name {
    position: absolute;
    left: 261px;
    top: 162px;
    margin: 0;
    font-size: 44px;
    font-weight: 400;
    line-height: 1.2;
    color: var(--text-light);
    white-space: nowrap;
  }
  .contact {
    position: absolute;
    left: 374px;
    top: 270px;
    margin: 0;
    font-size: 28px;
    font-weight: 400;
    line-height: 1.2;
    color: var(--text-soft);
    white-space: nowrap;
  }
  .ring {
    position: absolute;
    left: 0;
    top: 0;
    width: 828px;
    height: 477px;
  }
  .vendor-mark {
    position: absolute;
    left: 34px;
    top: 408px;
    display: flex;
    align-items: center;
    gap: 7px;
  }
  .vendor-mark__seal {
    width: 24px;
    height: 24px;
    border-radius: 50%;
    background: var(--seal-gold);
  }
  .vendor-mark__name {
    font-size: 22px;
    line-height: 1.2;
    color: var(--text-light);
  }
</style>
</head>
<body>
<div class="canvas">
  <section class="card card--front">
    <span class="brand-ring" aria-hidden="true"></span>
    <h1 class="wordmark">Trade with Tilda</h1>
  </section>

  <section class="card card--back">
    <div class="band"></div>
    <svg class="ring" viewBox="0 0 828 477" aria-hidden="true">
      <circle cx="88" cy="437" r="78" fill="none" stroke="var(--ring-blue)" stroke-width="18"/>
    </svg>
    <h2 class="holder-name">Tilda Marlowe</h2>
    <p class="contact">Contact: 0492716045</p>
    <div class="vendor-mark">
      <span class="vendor-mark__seal"></span>
      <span class="vendor-mark__name">Bidnest</span>
    </div>
  </section>
</div>
</body>
</html>
```